Halden Construction Inc Business Card Design

We want a business card that stands out; we build high end commercial interiors so card should be professional yet creative and have an architectural/design feel , very clean lines

We have 6 employees so we must be able to change the name, cell and email on each person's card
For the proof Paul Merriton is the president
Office Number is (555) 284-3916, Cell ( 555 ) 431-0827

4700 Calloway Lane Suite 305, Cedar Harbor Springs, FL 34108
www.haldenbuilds.com
CGC 374915 ( This license must legally be on card)

Target Market(s)

Asset Specialists , Developers, Building owners, architects, business owners

Industry/Entity Type

Construction Company

Contact Information for Business Card

We want a very high end clean look, must incorporate existing logo

Font styles to use
Other font styles liked:
• Gotham, trade gothic, Mrs. Eaves,modern 20, trim or designers' choice

Colors

Designer to choose colors to be used in the design.

Requirements
Must have
• Name, address, CGC 374915, www.haldenbuilds.com
• 4700 Calloway Lane Suite 305, Cedar Harbor Springs, FL 34108
• each persons name, cell phone and individual email address ie paulm@haldenbuilds.com

```html
<!DOCTYPE html>
<html lang="en">
<head>
<meta charset="utf-8">
<title>Halden Construction Inc Business Card</title>
<link rel="stylesheet" href="https://fonts.googleapis.com/css2?family=Montserrat:wght@500;600;700&family=Josefin+Sans:wght@600&display=swap">
<style>
  :root {
    --backdrop: #000000;
    --navy: #2b2f86;
    --navy-deep: #262a78;
    --navy-light: #33389a;
    --green: #7ac143;
    --white: #ffffff;
    --paper: #ffffff;
  }
  * { margin: 0; padding: 0; box-sizing: border-box; }
  html, body {
    width: 1200px; height: 1000px; overflow: hidden;
    background: var(--backdrop);
  }
  .canvas { position: relative; width: 1200px; height: 1000px; }

  .card { position: absolute; left: 258px; width: 683px; height: 390px; overflow: hidden; }

  /* Front */
  .card-front { top: 94px; }
  .front-texture {
    position: absolute; inset: 0;
    background: linear-gradient(135deg, var(--navy-light) 0%, var(--navy) 50%, var(--navy-deep) 100%);
  }
  .front-wordmark {
    position: absolute; left: 0; right: 0; top: 172px;
    display: flex; align-items: center; justify-content: center; gap: 16px;
    font-family: "Josefin Sans", sans-serif; font-weight: 600; white-space: nowrap;
    color: var(--white); font-size: 34px; line-height: 40px; letter-spacing: 4px; text-transform: uppercase;
  }
  .front-wordmark .mark-dot {
    width: 28px; height: 28px; border-radius: 50%; background: var(--white); flex: none;
  }

  /* Back */
  .card-back { top: 520px; background: var(--paper); }
  .back-wordmark {
    position: absolute; left: 20px; top: 92px;
    display: flex; align-items: center; gap: 10px;
    font-family: "Josefin Sans", sans-serif; font-weight: 600; white-space: nowrap;
    color: var(--navy); font-size: 24px; line-height: 28px; letter-spacing: 2px; text-transform: uppercase;
  }
  .back-wordmark .mark-dot {
    width: 20px; height: 20px; border-radius: 50%; background: var(--navy); flex: none;
  }
  .person {
    position: absolute; right: 24px; top: 151px; text-align: right;
    font-family: "Montserrat", sans-serif;
  }
  .person-name { color: var(--navy); font-weight: 700; font-size: 21px; line-height: 26px; }
  .person-title { color: var(--green); font-weight: 600; font-size: 16px; line-height: 20px; }

  .accent-rule {
    position: absolute; left: 14px; top: 207px; width: 653px; height: 8px;
    background: var(--green);
  }
  .info-panel {
    position: absolute; left: 14px; top: 224px; width: 653px; height: 152px;
    background: linear-gradient(135deg, var(--navy-light), var(--navy-deep));
    font-family: "Montserrat", sans-serif; color: var(--white);
  }
  .rule-node {
    position: absolute; left: 594px; top: 203px; width: 34px; height: 34px;
    border-radius: 50%; background: var(--navy); border: 4px solid var(--white);
  }
  .contact-list { position: absolute; left: 16px; top: 24px; list-style: none; }
  .contact-list li {
    display: flex; align-items: center; height: 28.5px;
    font-size: 16.5px; font-weight: 500; white-space: nowrap;
  }
  .contact-list svg { width: 22px; height: 22px; margin-right: 14px; flex: none; }
  .address {
    position: absolute; left: 350px; top: 24px; display: flex;
    font-size: 16px; font-weight: 600; line-height: 25px; white-space: nowrap;
  }
  .address svg { width: 20px; height: 24px; margin-right: 8px; flex: none; }
  .license {
    position: absolute; right: 8px; bottom: 8px;
    color: var(--green); font-style: italic; font-weight: 600; font-size: 14px; letter-spacing: 0.5px;
  }
</style>
</head>
<body>
<div class="canvas">

  <section class="card card-front">
    <div class="front-texture" role="img" aria-label="Subtle navy diamond lattice background texture"></div>
    <div class="front-wordmark"><span class="mark-dot"></span><span>Halden Construction</span></div>
  </section>

  <section class="card card-back">
    <div class="back-wordmark"><span class="mark-dot"></span><span>Halden Construction</span></div>

    <div class="person">
      <div class="person-name">PAUL MERRITON</div>
      <div class="person-title">president</div>
    </div>

    <div class="accent-rule"></div>

    <div class="info-panel" role="group" aria-label="Contact details">
      <ul class="contact-list">
        <li>
          <svg viewBox="0 0 24 24" fill="none" stroke="var(--green)" stroke-width="2"><rect x="7" y="2" width="10" height="20" rx="2"/><line x1="11" y1="18" x2="13" y2="18"/></svg>
          (555) 284-3916
        </li>
        <li>
          <svg viewBox="0 0 24 24" fill="var(--green)"><path d="M3 9c0-3 4-5 9-5s9 2 9 5v2h-5V9H8v2H3z"/><path d="M6 12h12l2 8H4z"/></svg>
          (555) 431-0827
        </li>
        <li>
          <svg viewBox="0 0 24 24" fill="var(--green)"><path d="M2 5h20v14H2z"/><path d="M2 5l10 8 10-8" fill="none" stroke="var(--navy)" stroke-width="1.6"/></svg>
          paulm@haldenbuilds.com
        </li>
        <li>
          <svg viewBox="0 0 24 24" fill="none" stroke="var(--green)" stroke-width="1.8"><circle cx="12" cy="12" r="10"/><ellipse cx="12" cy="12" rx="4.5" ry="10"/><line x1="2" y1="12" x2="22" y2="12"/><line x1="4" y1="7" x2="20" y2="7"/><line x1="4" y1="17" x2="20" y2="17"/></svg>
          www.haldenbuilds.com
        </li>
      </ul>

      <div class="address">
        <svg viewBox="0 0 20 24" fill="none" stroke="var(--green)" stroke-width="2.2"><path d="M10 22C4 14 3 11 3 9a7 7 0 0 1 14 0c0 2-1 5-7 13z"/><circle cx="10" cy="9" r="2.5"/></svg>
        <div>4700 Calloway Lane Suite 305,<br>Cedar Harbor Springs, FL 34108</div>
      </div>

      <div class="license">LICENSE: CGC 374915</div>
    </div>

    <div class="rule-node"></div>
  </section>

</div>
</body>
</html>
```